Exciting new branding of Recruitment Company based on it's new website

We have an exciting new website we are about to launch and would like to have letterhead, business cards, email signature options, email banner, linkedin and facebook cover images all refreshed to match the website. I have attached the existing logo. The website is at http://brightcrewhire.samplehost.com/ and we are particularly interested in the grey with orange writing at the base of the first page where it says Register Now

Target Market(s)

Recruitment

Contact Information for Business Card

Dana Holt
Account Executive
T: 1300 582 317
M: 0412 637 845
E: dana@brightcrewhire.com.au
W: brightcrewhire.com.au
A: Suite 3, 42 Tamsin Court, Carrow Vale ACT 2915
ABN: 52 418 736 904

Font styles to use
Serif
Sans Serif

Requirements
Must have
• The grey colour from the website

```html
<!DOCTYPE html>
<html lang="en">
<head>
<meta charset="utf-8">
<title>Bright Crew Hire – Business Card</title>
<link rel="stylesheet" href="https://fonts.googleapis.com/css2?family=Poppins:wght@700&family=Roboto:wght@400;700&display=swap">
<style>
  :root {
    --orange: #eba03f;
    --paper: #f3f3f3;
    --grey: #555759;
    --ink: #3a3b3d;
    --backdrop: #e6e5e3;
  }
  * { margin: 0; padding: 0; box-sizing: border-box; }
  html, body { width: 1200px; height: 960px; overflow: hidden; }
  body {
    background: var(--backdrop);
    font-family: "Roboto", Arial, sans-serif;
    position: relative;
  }
  .card {
    position: absolute;
    left: 270px;
    width: 660px;
    height: 403px;
    overflow: hidden;
    box-shadow: 0 6px 18px rgba(0,0,0,0.12);
  }
  .card--front { top: 50px; background: var(--orange); }
  .card--back { top: 507px; background: var(--paper); }

  .brand { position: absolute; display: flex; align-items: center; gap: 18px; }
  .brand__mark { border-radius: 50%; flex: none; }
  .brand__name {
    font-family: "Poppins", Arial, sans-serif;
    font-weight: 700;
    line-height: 0.95;
    letter-spacing: -0.5px;
    white-space: nowrap;
  }
  .card--front .brand { left: 50%; top: 50%; transform: translate(-50%, -50%); }
  .card--front .brand__mark { width: 96px; height: 96px; background: #fff; }
  .card--front .brand__name { font-size: 50px; color: #fff; }

  .card--back .brand { left: 58px; top: 120px; gap: 12px; }
  .card--back .brand__mark { width: 62px; height: 62px; background: var(--orange); }
  .card--back .brand__name { font-size: 28px; color: var(--orange); }

  .divider {
    position: absolute;
    left: 318px; top: 82px;
    width: 1.5px; height: 176px;
    background: var(--grey);
  }
  .contact { position: absolute; left: 338px; top: 80px; color: var(--grey); white-space: nowrap; }
  .contact__name { font-weight: 700; font-size: 22px; color: var(--orange); line-height: 1.05; }
  .contact__role { font-weight: 700; font-size: 14px; color: var(--ink); margin-bottom: 10px; }
  .contact__abn { font-size: 15px; margin-bottom: 4px; }
  .contact__list { list-style: none; }
  .contact__item { display: flex; align-items: center; gap: 7px; font-size: 15px; line-height: 22px; }
  .contact__icon { width: 13px; height: 13px; flex: none; }

  .address-band {
    position: absolute;
    left: 0; right: 0; top: 300px; height: 50px;
    background: var(--orange);
    color: #fff;
    display: flex; align-items: center; justify-content: center; gap: 8px;
    font-size: 17px;
    white-space: nowrap;
  }
  .address-band__icon { width: 14px; height: 18px; flex: none; }
</style>
</head>
<body>

<section class="card card--front" aria-label="Business card front">
  <div class="brand">
    <span class="brand__mark"></span>
    <span class="brand__name">bright crew<br>hire</span>
  </div>
</section>

<section class="card card--back" aria-label="Business card back">
  <div class="brand">
    <span class="brand__mark"></span>
    <span class="brand__name">bright crew<br>hire</span>
  </div>

  <div class="divider"></div>

  <div class="contact">
    <p class="contact__name">Dana Holt</p>
    <p class="contact__role">Account Executive</p>
    <p class="contact__abn">ABN: 52 418 736 904</p>
    <ul class="contact__list">
      <li class="contact__item">
        <svg class="contact__icon" viewBox="0 0 13 13"><rect x="3" y="0.5" width="7" height="12" rx="1.2" fill="none" stroke="#eba03f" stroke-width="1.4"/><circle cx="6.5" cy="10.3" r="0.8" fill="#eba03f"/></svg>
        0412 637 845
      </li>
      <li class="contact__item">
        <svg class="contact__icon" viewBox="0 0 13 13"><path d="M1 5 Q6.5 0 12 5 L10 6.5 L8.5 4.8 L4.5 4.8 L3 6.5 Z" fill="#eba03f"/><rect x="2.5" y="7" width="8" height="5" rx="1" fill="#eba03f"/></svg>
        1300 582 317
      </li>
      <li class="contact__item">
        <svg class="contact__icon" viewBox="0 0 13 13"><rect x="0.5" y="2.5" width="12" height="8.5" fill="#eba03f"/><path d="M0.5 2.5 L6.5 7.5 L12.5 2.5" fill="none" stroke="#fff" stroke-width="1"/></svg>
        dana@brightcrewhire.com.au
      </li>
      <li class="contact__item">
        <svg class="contact__icon" viewBox="0 0 13 13"><circle cx="6.5" cy="6.5" r="6" fill="#eba03f"/><path d="M1 6.5 H12 M6.5 1 Q3 6.5 6.5 12 M6.5 1 Q10 6.5 6.5 12" fill="none" stroke="#fff" stroke-width="0.9"/></svg>
        brightcrewhire.com.au
      </li>
    </ul>
  </div>

  <div class="address-band">
    <svg class="address-band__icon" viewBox="0 0 14 18"><path d="M7 0.5 A6 6 0 0 1 13 6.5 C13 11 7 17.5 7 17.5 C7 17.5 1 11 1 6.5 A6 6 0 0 1 7 0.5 Z" fill="#fff"/><circle cx="7" cy="6.5" r="2.3" fill="#eba03f"/></svg>
    <span>Suite 3, 42 Tamsin Court, Carrow Vale ACT 2915</span>
  </div>
</section>

</body>
</html>
```